Website for boutique digital agency helping high-tech startups accelerate growth.

We need a website design for a relatively young company based in Mauritius called 'LoomTrax'.

We are a professional services firm delivering digital infrastructure for revenue operations (RevOps)*.

Entrepreneurial startups and SMBs in the technology sector work with us to accelerate growth by delivering extraordinary customer experiences across the full customer lifecycle.

We would like a colourful design that utilises the (4) colours of our existing logo design.

The final design should communicate dynamic growth through relentless customer focus.
----------------------------------------------------------
*Revenue Operations (RevOps) is the strategic alignment of sales, marketing and customer success operations to accelerate growth by delivering extraordinary customer experiences across the full customer life cycle.
Updates

Target Market(s)

Entrepreneurial startups and SMBs (Small/Medium Businesses) in the technology sector.

Question: Why the technology sector?

Answer: Because technology entrepreneurs often have a tremendous challenge to effectively communicate to the market and to prospective customers the value and the benefits of their products & services due to the inherent complexity of technological innovation.

LoomTrax is a team of creatively-minded engineers and technologists who have worked with and understand the technologies and innovations our clients are passionate about bringing to market.

Industry/Entity Type

Professional Service

Number of Pages Required

5+ page

Font styles to use
Sans Serif

Requirements
Must have
• Minimalistic designs rich with visual meaning are highly preferred. Mobile responsive designs are also required. Must show how designs render on Desktop, Tablet and Smartphone devices.

Website pages:
1) Homepage: problem statement, target customers, value proposition & benefits
2) Services: 3-4 tiers of services packages with pricing and "how to work with us"
3) Resources: links to all kinds of relevant materials
4) Contact Us: contact form and special project quote form
5) Blog: matrix design with featured images for each post
Nice to have
• Bold, interesting, colourful, inspiring images that visually communicate:
- relentless customer focus
- extraordinary, memorable experiences
- business at the speed of innovation
Should not have
• Any meme or theme that panders to "political correctness".

```html
<!DOCTYPE html>
<html lang="en">
<head>
<meta charset="utf-8">
<title>LoomTrax — Boutique Digital Agency</title>
<link rel="stylesheet" href="https://fonts.googleapis.com/css2?family=Poppins:wght@300;400;500;600;700;800&display=swap">
<style>
:root{
  --teal:#0e6b6a;
  --teal-deep:#0c5f73;
  --orange:#ff5b00;
  --red:#e8132e;
  --green:#7cc21b;
  --lime:#b4ec56;
  --ink:#2b2b2b;
  --muted:#6b6b6b;
  --soft:#f7f7f7;
  --line:#e4e4e4;
}
*{box-sizing:border-box;margin:0;padding:0}
html,body{width:1200px;height:4725px;overflow:hidden}
body{position:relative;background:#fff;font-family:'Poppins',sans-serif;color:var(--ink)}
.abs{position:absolute}
a{color:inherit;text-decoration:none}

/* header */
.site-header{position:absolute;top:0;left:0;width:1200px;height:80px;z-index:5}
.brand{position:absolute;left:165px;top:12px;display:flex;align-items:center;gap:8px;font-weight:700;font-size:21px;color:var(--ink)}
.brand-mark{width:20px;height:20px;background:var(--red);border-radius:50%}
.main-nav{position:absolute;left:382px;top:24px;display:flex;gap:30px;font-size:15px;color:var(--teal-deep)}
.main-nav .active{color:var(--orange)}
.header-phone{position:absolute;left:912px;top:24px;font-size:15px;font-weight:600;color:var(--orange);display:flex;align-items:center;gap:10px}

/* hero */
.hero-photo{left:486px;top:0;width:714px;height:590px}
.hero-copy{left:158px;top:188px;width:440px}
.hero-kicker{font-size:26px;font-weight:400;color:var(--ink);line-height:1.1}
.hero-sub{font-size:46px;font-weight:400;color:var(--ink);line-height:1.25}
.hero-title{font-size:74px;font-weight:800;color:var(--teal);line-height:1;letter-spacing:1px}
.hero-text{margin-top:14px;font-size:14px;line-height:1.45;color:#444;width:440px}
.btn{display:inline-block;background:var(--orange);color:#fff;font-weight:600;font-size:13px;text-transform:uppercase;letter-spacing:.5px;text-align:center}
.hero-btn{margin-top:22px;width:134px;height:46px;line-height:46px}

/* section headings */
.eyebrow{font-size:28px;color:var(--teal);font-weight:400;text-align:center}
.section-title{font-size:44px;color:var(--teal);font-weight:400;text-align:center;line-height:1.1}
.section-title.bold{font-weight:700}

/* features */
.features-head{left:0;top:718px;width:1200px}
.feature-card{top:881px;width:209px;height:238px;background:#fff;box-shadow:0 4px 14px rgba(0,0,0,.12);padding:38px 12px 0 12px}
.feature-card h3{font-size:15px;font-weight:500;color:var(--teal);line-height:1.2;height:38px}
.feature-icon{margin:12px 0 0 6px;width:78px;height:64px}
.feature-rule{width:40px;height:2px;background:var(--red);margin:16px 0 8px 0}
.feature-card p{font-size:11.5px;color:#555;line-height:1.35}

/* value */
.value-band{left:0;top:1257px;width:1200px;height:514px;background:var(--soft)}
.split-title{font-size:44px;color:var(--teal);font-weight:400;line-height:1.05}
.split-text{font-size:14px;line-height:1.5;color:#444;margin-top:14px}

/* packages */
.plan{top:2609px;width:296px;height:349px;background:#fff;box-shadow:0 4px 16px rgba(0,0,0,.07);text-align:center;padding-top:52px;color:var(--teal-deep)}
.plan.featured{top:2587px;height:397px;background:var(--teal-deep);color:#fff;padding-top:74px;box-shadow:none}
.plan-name{font-size:17px}
.plan-price{font-size:44px;font-weight:700;color:var(--orange);line-height:1.15}
.plan-price small{font-size:22px;font-weight:400}
.plan-list{font-size:13px;line-height:2.15;margin-top:4px}
.plan-btn{margin-top:14px;width:134px;height:46px;line-height:46px}
.plan.featured .plan-btn{background:#fff;color:var(--orange)}

/* customers */
.client{top:3184px;width:209px;height:97px;border:1px solid #ddd;display:flex;align-items:center;justify-content:center;gap:9px;font-size:22px;font-weight:600;color:#3a3a3a;background:#fff}
.client-dot{width:16px;height:16px;border-radius:50%;background:#444}
.pager{left:582px;top:3320px;display:flex;gap:8px}
.pager span{width:6px;height:6px;border-radius:50%;background:#ccc}
.pager .on{background:var(--teal-deep)}

/* blog */
.post{top:3492px;width:283px}
.post-img{width:283px;height:183px;box-shadow:0 3px 10px rgba(0,0,0,.15)}
.post-date{margin-top:16px;font-size:13px;color:#888}
.post-title{font-size:17px;line-height:1.15;color:var(--ink);margin-top:4px;font-weight:400}
.post-more{display:block;margin-top:16px;font-size:12px;font-weight:700;color:var(--teal-deep)}

/* contact */
.contact-band{left:0;top:3872px;width:1200px;height:455px;overflow:hidden}
.contact-form{left:370px;top:3970px;width:460px;color:#fff}
.contact-form h2{font-size:42px;font-weight:400;text-align:center;margin-bottom:22px}
.field-row{display:flex;gap:16px;margin-bottom:34px}
.field{flex:1;font-size:11px;border-bottom:1px solid rgba(255,255,255,.6);padding-bottom:8px}
.submit-btn{display:block;margin:0 auto;width:134px;height:44px;line-height:44px}

/* footer */
.site-footer{left:0;top:4327px;width:1200px;height:398px;background:var(--soft)}
.foot-col h4{font-size:15px;font-weight:600;color:var(--teal-deep);margin-bottom:16px}
.foot-col p,.foot-col li{font-size:11.5px;line-height:1.75;color:var(--teal-deep);list-style:none}
.foot-contact{display:flex;align-items:center;gap:14px;font-size:12px;color:var(--teal-deep);margin-top:6px}
.foot-contact i{width:10px;height:10px;background:var(--orange);display:inline-block;border-radius:2px}
.social{display:flex;gap:12px;margin-top:8px}
.social span{width:14px;height:14px;background:var(--teal-deep);border-radius:50%}
.news-input{width:226px;height:40px;background:#e6e6e6;font-size:11px;color:#444;padding:12px 10px;margin-top:4px}
.news-btn{margin-top:14px;width:134px;height:46px;line-height:46px}
.foot-rule{left:158px;top:4661px;width:884px;height:1px;background:var(--line)}
.copyright{left:0;top:4686px;width:1200px;text-align:center;font-size:12px;color:var(--teal-deep)}
</style>
</head>
<body>

<header class="site-header">
  <a class="brand" href="#"><span class="brand-mark"></span>loomtrax.io</a>
  <nav class="main-nav">
    <a class="active" href="#">Home</a><a href="#">Services</a><a href="#">Resources</a><a href="#">Blog</a><a href="#">Contact Us</a>
  </nav>
  <div class="header-phone">
    <svg width="18" height="18" viewBox="0 0 18 18"><circle cx="9" cy="9" r="9" fill="#fff0e6"/><path d="M6 4.5c.6 0 1.8 2 1.5 2.5l-.8.8c.4 1.2 1.3 2.3 2.5 2.8l.8-.8c.5-.3 2.5.9 2.5 1.5 0 .8-1 1.9-2 1.7C7.5 12.5 5.2 10 4.5 7c-.2-1 .9-2.5 1.5-2.5z" fill="var(--orange)"/></svg>
    555-010-2040
  </div>
</header>

<!-- hero -->
<svg class="abs hero-photo" viewBox="0 0 714 590" role="img" aria-label="Photo of a small team gathered around a laptop in a bright office">
  <defs>
    <linearGradient id="heroG" x1="0" y1="0" x2="1" y2="1">
      <stop offset="0" stop-color="#efe7dd"/><stop offset=".55" stop-color="#c9a88a"/><stop offset="1" stop-color="#6d5647"/>
    </linearGradient>
  </defs>
  <path d="M30 220C50 110 150 40 300 20L714 0V370C650 500 520 590 380 585C230 580 110 520 60 420C25 350 20 280 30 220Z" fill="url(#heroG)"/>
  <path d="M70 0C20 70 5 150 25 240" fill="none" stroke="var(--green)" stroke-width="7"/>
</svg>
<div class="abs hero-copy">
  <p class="hero-kicker">We are</p>
  <p class="hero-sub">Boutique</p>
  <h1 class="hero-title">DIGITAL<br>AGENCY</h1>
  <p class="hero-text">Many desktop publishing packages and web page editors now use Lorem Ipsum as their default model text, and a search for 'lorem ipsum'</p>
  <a class="btn hero-btn" href="#">Contact us</a>
</div>

<!-- features -->
<svg class="abs" style="left:100px;top:800px" width="330" height="370" viewBox="0 0 330 370" aria-hidden="true">
  <path d="M10 120C20 40 120 0 210 40C270 70 320 130 290 220C260 300 150 330 80 300C20 270 0 200 10 120Z" fill="#f3f3f3"/>
</svg>
<div class="abs features-head">
  <p class="eyebrow">Features</p>
  <h2 class="section-title">Provide Awesome Service<br>With Our Tools</h2>
</div>

<article class="abs feature-card" style="left:158px">
  <h3>Connectivity<br>and transportation</h3>
  <svg class="feature-icon" viewBox="0 0 78 64"><path d="M8 30C6 12 24 2 46 4C66 6 78 20 72 38C66 56 42 62 24 56C12 52 9 42 8 30Z" fill="var(--teal)"/><rect x="30" y="18" width="18" height="24" rx="2" fill="none" stroke="#fff" stroke-width="2"/><path d="M24 26h6M24 34h6M48 26h6M48 34h6" stroke="#fff" stroke-width="2"/></svg>
  <div class="feature-rule"></div>
  <p>long established fact that a reader will be distracted</p>
</article>
<article class="abs feature-card" style="left:384px">
  <h3>Storage and<br>processing</h3>
  <svg class="feature-icon" viewBox="0 0 78 64"><path d="M8 30C6 12 24 2 46 4C66 6 78 20 72 38C66 56 42 62 24 56C12 52 9 42 8 30Z" fill="var(--red)"/><circle cx="39" cy="30" r="12" fill="none" stroke="#fff" stroke-width="2"/><path d="M39 24v12M34 30l5-6 5 6" fill="none" stroke="#fff" stroke-width="2"/></svg>
  <div class="feature-rule"></div>
  <p>long established fact that a reader will be distracted</p>
</article>
<article class="abs feature-card" style="left:607px">
  <h3>Services and<br>applications</h3>
  <svg class="feature-icon" viewBox="0 0 78 64"><path d="M8 30C6 12 24 2 46 4C66 6 78 20 72 38C66 56 42 62 24 56C12 52 9 42 8 30Z" fill="var(--green)"/><rect x="27" y="19" width="24" height="22" rx="2" fill="none" stroke="#fff" stroke-width="2"/><circle cx="39" cy="31" r="5" fill="none" stroke="#fff" stroke-width="2"/></svg>
  <div class="feature-rule"></div>
  <p>long established fact that a reader will be distracted</p>
</article>
<article class="abs feature-card" style="left:833px">
  <h3>Terminals and<br>devices</h3>
  <svg class="feature-icon" viewBox="0 0 78 64"><path d="M8 30C6 12 24 2 46 4C66 6 78 20 72 38C66 56 42 62 24 56C12 52 9 42 8 30Z" fill="var(--orange)"/><rect x="28" y="18" width="22" height="18" rx="2" fill="none" stroke="#fff" stroke-width="2"/><path d="M33 42h12M39 36v6" stroke="#fff" stroke-width="2"/></svg>
  <div class="feature-rule"></div>
  <p>long established fact that a reader will be distracted</p>
</article>

<!-- value proposition -->
<section class="abs value-band"></section>
<div class="abs" style="left:158px;top:1398px;width:430px">
  <h2 class="split-title">Value proposition &amp;<br>Benefits</h2>
  <p class="split-text">It is a long established fact that a reader will be distracted by the readable content of a page when looking at its layout. The point of using Lorem Ipsum is that it has a more-or-less normal distribution of letters, as opposed to using 'Content here, content here', making it look like readable English.</p>
</div>
<svg class="abs" style="left:639px;top:1285px" width="561" height="467" viewBox="0 0 561 467" role="img" aria-label="Photo of a smiling professional at her desk, tinted in orange tones">
  <defs>
    <linearGradient id="valG" x1="0" y1="0" x2="1" y2="1">
      <stop offset="0" stop-color="#f0a12a"/><stop offset=".5" stop-color="#f06a22"/><stop offset="1" stop-color="#a7b6c8"/>
    </linearGradient>
  </defs>
  <path d="M10 250C0 150 90 60 200 30C300 5 420 0 500 60C560 110 570 230 540 320C500 420 400 470 290 460C160 450 20 380 10 250Z" fill="url(#valG)"/>
</svg>

<!-- problem statement -->
<svg class="abs" style="left:0;top:1844px" width="550" height="496" viewBox="0 0 550 496" role="img" aria-label="Photo of a man working on a laptop, tinted in teal">
  <defs>
    <linearGradient id="probG" x1="0" y1="0" x2="1" y2="1">
      <stop offset="0" stop-color="#2fb8b2"/><stop offset=".6" stop-color="#1a8f8f"/><stop offset="1" stop-color="#1e3f44"/>
    </linearGradient>
  </defs>
  <path d="M0 70C80 20 200 0 300 10C420 20 540 60 548 170C556 280 480 420 360 470C250 510 130 480 60 420C20 390 0 350 0 320Z" fill="url(#probG)"/>
</svg>
<div class="abs" style="left:607px;top:1965px;width:430px">
  <h2 class="split-title">Problem statement</h2>
  <p class="split-text">It is a long established fact that a reader will be distracted by the readable content of a page when looking at its layout.<br>The point of using Lorem Ipsum is that it has a more-or-less normal distribution of letters, as opposed to using 'Content here, content here', making it look like readable English.</p>
</div>

<!-- packages -->
<svg class="abs" style="left:0;top:2455px" width="1200" height="620" viewBox="0 0 1200 620" aria-hidden="true">
  <path d="M0 10C90 0 220 50 280 150C200 200 120 300 70 420C40 460 20 470 0 470Z" fill="var(--lime)"/>
  <path d="M110 590C60 620 40 700 60 780" fill="none" stroke="#e6e6e6" stroke-width="2"/>
</svg>
<div class="abs" style="left:0;top:2485px;width:1200px">
  <p class="eyebrow">Packages</p>
  <h2 class="section-title bold">The best packages for our client</h2>
</div>
<div class="abs plan" style="left:158px">
  <p class="plan-name">Basic Plan</p>
  <p class="plan-price"><small>$</small>25</p>
  <p class="plan-list">Lorem Ipsum<br>is simply dummy text<br>the printing<br>and typesetting industry.</p>
  <a class="btn plan-btn" href="#">Get started</a>
</div>
<div class="abs plan featured" style="left:453px">
  <p class="plan-name">Standart Plan</p>
  <p class="plan-price"><small>$</small>55</p>
  <p class="plan-list">Lorem Ipsum<br>is simply dummy text<br>the printing<br>and typesetting industry.</p>
  <a class="btn plan-btn" href="#">Get started</a>
</div>
<div class="abs plan" style="left:749px">
  <p class="plan-name">Premium Plan</p>
  <p class="plan-price"><small>$</small>85</p>
  <p class="plan-list">Lorem Ipsum<br>is simply dummy text<br>the printing<br>and typesetting industry.</p>
  <a class="btn plan-btn" href="#">Get started</a>
</div>

<!-- target customers -->
<div class="abs" style="left:0;top:3108px;width:1200px">
  <h2 class="section-title">Target Customers</h2>
</div>
<div class="abs client" style="left:158px"><span class="client-dot"></span>Kestrel</div>
<div class="abs client" style="left:384px"><span class="client-dot"></span>Norvane</div>
<div class="abs client" style="left:607px"><span class="client-dot"></span>Tacora</div>
<div class="abs client" style="left:833px"><span class="client-dot"></span>Verdeo</div>
<div class="abs pager"><span></span><span class="on"></span><span></span></div>

<!-- blog -->
<svg class="abs" style="left:750px;top:3300px" width="450" height="380" viewBox="0 0 450 380" aria-hidden="true">
  <path d="M10 160C10 60 120 0 260 10C360 18 450 60 450 60V380H120C50 340 10 260 10 160Z" fill="#f6f6f6"/>
</svg>
<div class="abs" style="left:0;top:3420px;width:1200px">
  <h2 class="section-title">Blog</h2>
</div>
<article class="abs post" style="left:158px">
  <div class="post-img" role="img" aria-label="Photo of colleagues meeting over lunch with a laptop" style="background:linear-gradient(135deg,#6b5a48,#c9b8a2 55%,#3f4a52)"></div>
  <p class="post-date">APRIL 6 , 2020</p>
  <h3 class="post-title">Lorem Ipsum has been the industry's standard</h3>
  <a class="post-more" href="#">READ MORE</a>
</article>
<article class="abs post" style="left:459px">
  <div class="post-img" role="img" aria-label="Photo of a hand reviewing printed charts with a pen" style="background:linear-gradient(135deg,#f1f1f3,#d8dbe6 55%,#b9a8c8)"></div>
  <p class="post-date">APRIL 6 , 2020</p>
  <h3 class="post-title">Lorem Ipsum has been the industry's standard</h3>
  <a class="post-more" href="#">READ MORE</a>
</article>
<article class="abs post" style="left:758px">
  <div class="post-img" role="img" aria-label="Photo of a team celebrating around a laptop" style="background:linear-gradient(135deg,#e9ecef,#c58d7a 55%,#7b4a3e)"></div>
  <p class="post-date">APRIL 6 , 2020</p>
  <h3 class="post-title">Lorem Ipsum has been the industry's standard</h3>
  <a class="post-more" href="#">READ MORE</a>
</article>

<!-- contact -->
<section class="abs contact-band">
  <div role="img" aria-label="Photo of a business team meeting around a boardroom table" style="position:absolute;inset:0;background:linear-gradient(90deg,#8c8f90 0%,#d9dcdd 30%,#eef0f0 60%,#c9cccc 100%)"></div>
  <svg style="position:absolute;left:0;top:0" width="1200" height="455" viewBox="0 0 1200 455" aria-hidden="true">
    <path d="M560 40C700 0 850 50 950 130C1020 190 1010 330 930 420L880 455H620C700 400 760 300 700 200C660 130 600 90 560 40Z" fill="var(--orange)"/>
    <path d="M330 160C380 70 510 20 640 30C780 40 900 110 910 220C920 330 820 420 680 440C530 460 380 420 320 330C290 280 300 210 330 160Z" fill="#8fc21a" fill-opacity=".93"/>
  </svg>
</section>
<form class="abs contact-form">
  <h2>Contact Us</h2>
  <div class="field-row"><div class="field">Your Name :</div><div class="field">Your Emai :</div></div>
  <div class="field-row"><div class="field">Phone :</div><div class="field">Message :</div></div>
  <a class="btn submit-btn" href="#">Submit now</a>
</form>

<!-- footer -->
<footer class="abs site-footer"></footer>
<div class="abs foot-col" style="left:158px;top:4390px;width:210px">
  <h4>ABOUT</h4>
  <p>It is a long established fact that a reader will be distracted by the readable content of a page when looking at its layout.</p>
  <div class="foot-contact" style="margin-top:14px"><i></i>Call us: +555.010.2040</div>
  <div class="foot-contact"><i></i>Email: hello@loomtrax.io</div>
  <h4 style="margin:22px 0 4px">CONNECT WITH US</h4>
  <div class="social" aria-label="Social links"><span></span><span></span><span></span><span></span><span></span></div>
</div>
<div class="abs foot-col" style="left:448px;top:4390px">
  <h4>SERVICE</h4>
  <ul><li>Connectivity</li><li>Storage</li><li>Services</li><li>Teminals</li></ul>
</div>
<div class="abs foot-col" style="left:595px;top:4390px">
  <h4>RESOURCES</h4>
  <ul><li>It is a long established</li><li>That a reader will be</li><li>Distracted by the readable</li><li>Content of a page</li></ul>
</div>
<div class="abs foot-col" style="left:815px;top:4390px;width:230px">
  <h4>NEWSLETTER</h4>
  <p>Subscribe to our newsletter to receive exclusive offers and wedding tips.</p>
  <div class="news-input" style="margin-top:14px">Enter Your mail ID</div>
  <a class="btn news-btn" href="#">Submit now</a>
</div>
<div class="abs foot-rule"></div>
<p class="abs copyright">Copyright©loomtrax All Rights Reserved.</p>

</body>
</html>
```